Medical group practice

We need a flyer design incorporating the three doctors in the practice, there is a general practitioner, ophthalmologist and an obstetrician & Gynaecologist. see the attached file for the concept. will leave the colour design up to you

Target Market(s)

general public

Industry/Entity Type

Health Care

Colors

Designer to choose colors to be used in the design.

Requirements
Must have
• logos included in attachement

```html
<!DOCTYPE html>
<html lang="en">
<head>
<meta charset="utf-8">
<title>Clearwell Medical Flyer</title>
<link href="https://fonts.googleapis.com/css2?family=Arimo:wght@400;700&display=swap" rel="stylesheet">
<style>
  :root {
    --backdrop: #8d9296;
    --paper: #ffffff;
    --brand-red: #c8202f;
    --deep-red: #8f1420;
    --ink: #1e1e1e;
    --muted: #555a5e;
    --footer: #151515;
    --photo-warm: #e9c9a8;
    --photo-cool: #b9c9c9;
    --icon-blue: #1d5d9b;
    --icon-teal: #3aa0c8;
  }
  * { box-sizing: border-box; margin: 0; padding: 0; }
  html, body { width: 1200px; height: 900px; overflow: hidden; }
  body {
    background: var(--backdrop);
    font-family: "Arimo", Arial, sans-serif;
    color: var(--ink);
  }
  .flyer {
    position: absolute; left: 255px; top: 10px;
    width: 690px; height: 880px;
    background: var(--paper);
    overflow: hidden;
  }
  .brand {
    position: absolute; left: 0; right: 0; top: 40px;
    text-align: center;
  }
  .brand-line { display: inline-flex; align-items: center; gap: 14px; }
  .brand-dot { width: 30px; height: 30px; border-radius: 50%; background: var(--brand-red); }
  .brand-name {
    font-weight: 700; font-size: 34px; letter-spacing: 2px;
    color: var(--brand-red); text-transform: uppercase;
  }
  .tagline { margin-top: 6px; font-size: 25px; color: var(--muted); }
  .photo {
    position: absolute; left: 0; top: 150px; width: 690px; height: 300px;
    background: linear-gradient(100deg, var(--photo-cool) 0%, var(--photo-warm) 40%, #f1dcc4 65%, var(--photo-cool) 100%);
  }
  .frame { position: absolute; left: 0; top: 0; width: 690px; height: 520px; }
  .service-icon {
    position: absolute; top: 378px; width: 150px; height: 150px; border-radius: 50%;
    background: var(--paper); border: 7px solid var(--brand-red);
    box-shadow: 0 3px 8px rgba(0,0,0,.3);
    display: flex; align-items: center; justify-content: center;
  }
  .service-icon .art { width: 112px; height: 112px; border-radius: 50%; }
  .icon-gp { left: 45px; }
  .icon-gp .art { background: radial-gradient(circle, var(--icon-teal), var(--icon-blue)); }
  .icon-eye { left: 270px; }
  .icon-eye .art { background: radial-gradient(circle, #6fa8d8, #e8eef4 70%); }
  .icon-obgyn { left: 495px; }
  .icon-obgyn .art { background: linear-gradient(120deg, #1f3f7a 50%, #4aa84a 50%); }
  .doctors {
    position: absolute; left: 30px; top: 550px; width: 640px; height: 186px;
    display: grid; grid-template-columns: 1fr 1fr 1fr;
  }
  .doctor { padding: 0 12px; font-size: 10px; line-height: 1.35; }
  .doctor + .doctor { border-left: 1px solid #999; }
  .doctor-name { font-weight: 700; font-size: 11.5px; line-height: 1.3; }
  .doctor-role { font-style: italic; font-size: 11px; }
  .doctor-email { font-size: 9.5px; margin-bottom: 8px; }
  .services { list-style: none; font-size: 10px; }
  .services li::before { content: "• "; }
  .address-bar {
    position: absolute; left: 0; top: 746px; width: 690px; height: 44px;
    background: linear-gradient(var(--brand-red), var(--deep-red));
    color: #fff; font-size: 19px;
    display: flex; justify-content: space-between; align-items: center; padding: 0 40px;
  }
  .footer {
    position: absolute; left: 0; top: 790px; width: 690px; height: 90px;
    background: var(--footer); color: #eee; font-size: 12px; line-height: 1.45;
    display: flex; padding: 14px 40px; gap: 60px;
  }
  .hours-title { font-weight: 700; }
  .lines { display: grid; grid-template-columns: 170px 1fr; column-gap: 30px; }
</style>
</head>
<body>
  <main class="flyer">
    <header class="brand">
      <div class="brand-line"><span class="brand-dot"></span><span class="brand-name">Clearwell Medical</span></div>
      <p class="tagline">Your Health Is Our Priority</p>
    </header>

    <div class="photo" role="img" aria-label="Photo of a smiling family of four relaxing together on a sofa"></div>

    <svg class="frame" viewBox="0 0 690 520" aria-hidden="true">
      <path d="M0 150 L0 215 Q345 115 690 215 L690 150 Z" fill="#ffffff"/>
      <path d="M0 215 Q345 115 690 215" fill="none" stroke="var(--brand-red)" stroke-width="8"/>
      <path d="M0 450 L690 450 L690 520 L0 520 Z" fill="#ffffff"/>
      <path d="M0 452 Q345 425 690 452" fill="none" stroke="var(--brand-red)" stroke-width="6"/>
    </svg>

    <div class="service-icon icon-gp"><div class="art" role="img" aria-label="General practice illustration with family and stethoscope"></div></div>
    <div class="service-icon icon-eye"><div class="art" role="img" aria-label="Ophthalmology illustration of an eye"></div></div>
    <div class="service-icon icon-obgyn"><div class="art" role="img" aria-label="Obstetrics illustration of mother and child"></div></div>

    <section class="doctors">
      <article class="doctor">
        <p class="doctor-name">Dr. Leon Harcourt, MD.</p>
        <p class="doctor-role">General Practitioner</p>
        <p class="doctor-email">Email: l.harcourt.clinic@mail.com</p>
        <ul class="services">
          <li>General Checks • Annual Check ups</li>
          <li>Wound Care/Dressings</li>
          <li>Incision &amp; Drainage</li>
          <li>Suturing Lacerations • Pain Injections</li>
          <li>Glucose Checks • Foreign Body Removal</li>
        </ul>
      </article>
      <article class="doctor">
        <p class="doctor-name">Dr. Elena R. Vasquez</p>
        <p class="doctor-role">MD. Surgeon Ophthalmologist</p>
        <p class="doctor-email">Email: elena.eyes@mail.com</p>
        <ul class="services">
          <li>Eyes disease examination</li>
          <li>Surgery of Pterygium • Cataract</li>
          <li>Glaucoma • Emergency Conjunctivitis</li>
          <li>Traumatism • Foreign body and more</li>
        </ul>
      </article>
      <article class="doctor">
        <p class="doctor-name">Dr. Arjun Mehra, BMedSci, MBBS, DM (O&amp;G), FACOG</p>
        <p class="doctor-role">Obstetrician &amp; Gynaecologist</p>
        <p class="doctor-email">Email: arjun.obgyn@mail.com</p>
        <ul class="services">
          <li>Obstetrics: Prenatal Care, Delivery, Postnatal checks, High Risk pregnancy</li>
          <li>Gynaecology: Pap smears, Abnormal Vaginal Bleeding, Fibroids, Colposcopy, Family Planning, Infertility, Cancer Screening, And More….</li>
        </ul>
      </article>
    </section>

    <div class="address-bar">
      <span>42 Harbour Road, Port Elling, Westmere</span>
      <span>Tel: (555) 210 4830 / 4831</span>
    </div>

    <footer class="footer">
      <div class="hours">
        <p class="hours-title">OPENING HOURS:</p>
        <p>Mondays - Fridays 9 am - 6 pm</p>
        <p>Saturdays - 10 am - 5 pm</p>
      </div>
      <div class="lines">
        <span>General Practitioner</span><span>- (555) 318 2245</span>
        <span>Ophthalmologist</span><span>- (555) 318 7702</span>
        <span>Obstetrician/Gynaecologist</span><span>- (555) 318 6190 / (555) 402 1187</span>
      </div>
    </footer>
  </main>
</body>
</html>
```